Fernly Garage Doors Business Card

I need a Business Card for my garage door business:
Fernly Garage Doors.
please add:
logo
phone number: 833-2-FERNLY
(337-659)

email: service@fernlygaragedoors.com
website: www.fernlygaragedoors.com

The attached image is recommendation ONLY.

```html
<!DOCTYPE html>
<html lang="en">
<head>
<meta charset="utf-8">
<title>Fernly Garage Doors – Business Card</title>
<link rel="stylesheet" href="https://fonts.googleapis.com/css2?family=Quicksand:wght@600&family=Open+Sans:wght@400&display=swap">
<style>
  :root {
    --backdrop: #3a3a3c;
    --card-light: #ffffff;
    --card-dark: #2a2a2c;
    --teal: #55c4d0;
    --ink: #1c1c1e;
    --ink-soft: #4a4a4e;
  }
  * { box-sizing: border-box; margin: 0; padding: 0; }
  html, body { width: 1200px; height: 800px; overflow: hidden; }
  body {
    background: var(--backdrop);
    display: flex;
    align-items: center;
    justify-content: center;
    gap: 50px;
  }
  .card {
    position: relative;
    width: 525px;
    height: 300px;
    border-radius: 4px;
    box-shadow: 0 14px 30px rgba(0,0,0,0.35);
  }
  .card--front { background: var(--card-light); }
  .card--back {
    background: var(--card-dark);
    display: flex;
    align-items: center;
    justify-content: center;
  }
  .contact-list {
    position: absolute;
    top: 46px;
    left: 200px;
    list-style: none;
    font-family: "Open Sans", sans-serif;
    font-size: 15px;
    color: var(--ink-soft);
  }
  .contact-list li {
    display: flex;
    align-items: center;
    gap: 10px;
    height: 24px;
  }
  .contact-list svg { width: 18px; height: 18px; flex: none; }
  .contact-phone-alt { margin-left: 26px; }
  .brand {
    display: flex;
    align-items: center;
    gap: 16px;
    font-family: "Quicksand", sans-serif;
    font-weight: 600;
  }
  .brand--front {
    position: absolute;
    left: 36px;
    bottom: 40px;
  }
  .brand-mark {
    width: 62px;
    height: 62px;
    border-radius: 50%;
    background: var(--teal);
    flex: none;
  }
  .brand-name {
    font-size: 30px;
    line-height: 1.05;
    color: var(--ink);
  }
  .brand--back .brand-mark { width: 78px; height: 78px; }
  .brand--back .brand-name { font-size: 36px; color: var(--teal); }
</style>
</head>
<body>
  <section class="card card--front" aria-label="Business card front">
    <ul class="contact-list">
      <li>
        <svg viewBox="0 0 24 24" aria-hidden="true"><path fill="var(--teal)" d="M6.6 10.8a15.1 15.1 0 0 0 6.6 6.6l2.2-2.2a1 1 0 0 1 1-.25 11.4 11.4 0 0 0 3.6.57 1 1 0 0 1 1 1V20a1 1 0 0 1-1 1A17 17 0 0 1 3 4a1 1 0 0 1 1-1h3.5a1 1 0 0 1 1 1c0 1.25.2 2.45.57 3.57a1 1 0 0 1-.25 1z"/></svg>
        <span>833-2-FERNLY</span><span class="contact-phone-alt">(337-659)</span>
      </li>
      <li>
        <svg viewBox="0 0 24 24" aria-hidden="true"><rect x="2" y="5" width="20" height="14" rx="1.5" fill="var(--teal)"/><path d="M3 6l9 7 9-7" fill="none" stroke="#fff" stroke-width="1.6"/></svg>
        <span>service@fernlygaragedoors.com</span>
      </li>
      <li>
        <svg viewBox="0 0 24 24" aria-hidden="true"><g fill="none" stroke="var(--teal)" stroke-width="2.6" stroke-linecap="round"><path d="M10 14a4 4 0 0 0 5.7 0l3-3a4 4 0 0 0-5.7-5.7l-1 1"/><path d="M14 10a4 4 0 0 0-5.7 0l-3 3a4 4 0 0 0 5.7 5.7l1-1"/></g></svg>
        <span>www.fernlygaragedoors.com</span>
      </li>
    </ul>
    <div class="brand brand--front">
      <span class="brand-mark" aria-hidden="true"></span>
      <span class="brand-name">Fernly<br>Garage Doors</span>
    </div>
  </section>

  <section class="card card--back" aria-label="Business card back">
    <div class="brand brand--back">
      <span class="brand-mark" aria-hidden="true"></span>
      <span class="brand-name">Fernly<br>Garage Doors</span>
    </div>
  </section>
</body>
</html>
```